Business Cards for a law firm

Business cards for our law firm. Use our silhoette logo and OAK HARBOR - check our website (www.oakharbor-legal.com)

Contact Information for Business Card

our silhouette logo, OAK HARBOR, 800-555-0147, Dorian Kestrup, dorian@oakharbor-legal.com

Requirements
Must have
• our silhouette logo, OAK HARBOR, 800-555-0147, Dorian Kestrup, dorian@oakharbor-legal.com

```html
<!DOCTYPE html>
<html lang="en">
<head>
<meta charset="utf-8">
<title>Oak Harbor – Business Cards</title>
<link rel="stylesheet" href="https://fonts.googleapis.com/css2?family=Montserrat:wght@500;600;700&family=Poppins:wght@400&display=swap">
<style>
  :root {
    --navy: #1b3068;
    --white: #ffffff;
    --stage: #6b6b6b;
  }
  * { box-sizing: border-box; margin: 0; padding: 0; }
  html, body { width: 1200px; height: 1015px; overflow: hidden; }
  body {
    background: var(--stage);
    font-family: "Montserrat", sans-serif;
    position: relative;
  }
  .card {
    position: absolute;
    left: 250px;
    width: 700px;
    height: 400px;
    box-shadow: 0 10px 24px rgba(0,0,0,.35);
  }
  .card-back { top: 90px; background: var(--navy); color: var(--white); }
  .card-front { top: 525px; background: var(--white); color: var(--navy); border-bottom: 12px solid var(--navy); }

  .brand { display: flex; align-items: center; gap: 18px; position: absolute; }
  .brand-mark { width: 44px; height: 44px; border-radius: 50%; }
  .card-back .brand-mark { background: var(--white); }
  .card-front .brand-mark { background: var(--navy); }
  .brand-name { font-weight: 700; font-size: 40px; letter-spacing: 5px; }

  .card-back .brand { left: 170px; top: 130px; }
  .back-phone { position: absolute; left: 220px; top: 245px; display: flex; align-items: center; gap: 22px; }
  .back-phone .icon-circle { width: 44px; height: 44px; border-radius: 50%; background: var(--white); display: flex; align-items: center; justify-content: center; }
  .back-phone .number { font-weight: 600; font-size: 36px; letter-spacing: 4px; }

  .card-front .brand { left: 130px; top: 60px; }
  .person-name { position: absolute; left: 200px; top: 150px; font-weight: 700; font-size: 26px; letter-spacing: 3px; }
  .name-rule { position: absolute; left: 200px; top: 192px; width: 90px; height: 2px; background: var(--navy); }
  .contact-list { position: absolute; left: 200px; top: 210px; list-style: none; font-family: "Poppins", sans-serif; }
  .contact-list li { display: flex; align-items: center; gap: 12px; height: 34px; font-size: 19px; }
  .contact-list li.phone { font-family: "Montserrat", sans-serif; font-weight: 600; font-size: 30px; height: 44px; }
  .contact-list .icon-circle { width: 28px; height: 28px; border: 1.5px solid var(--navy); border-radius: 50%; display: flex; align-items: center; justify-content: center; flex: none; }
</style>
</head>
<body>
  <section class="card card-back">
    <div class="brand">
      <span class="brand-mark"></span>
      <span class="brand-name">OAK HARBOR</span>
    </div>
    <div class="back-phone">
      <span class="icon-circle">
        <svg width="24" height="24" viewBox="0 0 24 24"><path d="M6.6 10.8a15 15 0 0 0 6.6 6.6l2.2-2.2a1 1 0 0 1 1-.25 11.4 11.4 0 0 0 3.6.6 1 1 0 0 1 1 1V20a1 1 0 0 1-1 1A17 17 0 0 1 3 4a1 1 0 0 1 1-1h3.5a1 1 0 0 1 1 1c0 1.25.2 2.45.6 3.6a1 1 0 0 1-.25 1z" fill="#1b3068"/></svg>
      </span>
      <span class="number">(800) 555-0147</span>
    </div>
  </section>

  <section class="card card-front">
    <div class="brand">
      <span class="brand-mark"></span>
      <span class="brand-name">OAK HARBOR</span>
    </div>
    <p class="person-name">DORIAN KESTRUP</p>
    <span class="name-rule"></span>
    <ul class="contact-list">
      <li class="phone">
        <span class="icon-circle"><svg width="14" height="14" viewBox="0 0 24 24"><path d="M6.6 10.8a15 15 0 0 0 6.6 6.6l2.2-2.2a1 1 0 0 1 1-.25 11.4 11.4 0 0 0 3.6.6 1 1 0 0 1 1 1V20a1 1 0 0 1-1 1A17 17 0 0 1 3 4a1 1 0 0 1 1-1h3.5a1 1 0 0 1 1 1c0 1.25.2 2.45.6 3.6a1 1 0 0 1-.25 1z" fill="#1b3068"/></svg></span>
        800-555-0147
      </li>
      <li>
        <span class="icon-circle"><svg width="14" height="14" viewBox="0 0 24 24"><rect x="2" y="5" width="20" height="14" fill="#1b3068"/><path d="M2 5l10 8 10-8" stroke="#fff" stroke-width="1.8" fill="none"/></svg></span>
        dorian@oakharbor-legal.com
      </li>
      <li>
        <span class="icon-circle"><svg width="14" height="14" viewBox="0 0 24 24" fill="none" stroke="#1b3068" stroke-width="2"><circle cx="12" cy="12" r="9"/><path d="M3 12h18M12 3c3 3 3 15 0 18M12 3c-3 3-3 15 0 18"/></svg></span>
        www.oakharbor-legal.com
      </li>
    </ul>
  </section>
</body>
</html>
```